Business Card Design

Freelance writer, coach, teacher and researcher specialising in improving mathematics teaching and learning in primary schools. I write books and articles for teachers, speak extensively at conferences in UK and aboard. Would like something with a cube in the design. Clean, modern - logo suitable for use on a website. Should NOT look 'childish' (no comic sans or chalkboard type fonts)

Full details to go on card:

Professor Dan Theroll
Unlocking Early Numeracy

info@dantheroll.net
#dantheroll26
www.dantheroll.net
+44 7812 660 394

Industry/Entity Type

Teacher

Contact Information for Business Card

Professor Dan Theroll
Unlocking Early Numbers

```html
<!DOCTYPE html>
<html lang="en">
<head>
<meta charset="utf-8">
<title>Professor Dan Theroll – Business Card</title>
<link rel="stylesheet" href="https://fonts.googleapis.com/css2?family=Source+Sans+3:wght@400;600&display=swap">
<style>
  :root {
    --page-bg: #e4e5e7;
    --card-white: #ffffff;
    --card-edge: #3a3a3a;
    --ink: #111111;
    --navy: #1d3a8a;
    --navy-tab: #0c2a6e;
    --green-light: #7fcf9f;
    --green-mid: #25b06f;
    --green-deep: #009a56;
    --earth: #5d3a17;
    --icon-red: #c8102e;
    --mint-soft: #d6ebdf;
    --mint-pale: #eef7f1;
  }
  html, body {
    margin: 0;
    width: 1200px;
    height: 1200px;
    overflow: hidden;
    background: var(--page-bg);
    font-family: "Source Sans 3", "Myriad Pro", Arial, sans-serif;
  }
  .business-card {
    position: absolute;
    left: 62px;
    top: 254px;
    width: 1077px;
    height: 693px;
    background: var(--card-white);
    outline: 1px solid var(--card-edge);
    overflow: hidden;
  }
  .cube-art-area {
    position: absolute;
    left: 505px;
    top: 0;
    width: 572px;
    height: 404px;
    background: radial-gradient(ellipse 60% 65% at 65% 40%, var(--mint-soft), var(--mint-pale) 100%);
  }
  .brand-mark {
    position: absolute;
    left: 147px;
    top: 82px;
    display: flex;
    align-items: center;
    gap: 12px;
    color: var(--navy);
    font-weight: 600;
    font-size: 30px;
  }
  .brand-mark .brand-square {
    width: 30px;
    height: 30px;
    background: var(--navy);
  }
  .identity {
    position: absolute;
    left: 70px;
    top: 166px;
  }
  .identity .person-name {
    margin: 0;
    font-weight: 600;
    font-size: 31px;
    line-height: 34px;
    color: var(--ink);
  }
  .identity .tagline {
    margin: 0;
    font-weight: 400;
    font-size: 30px;
    line-height: 34px;
    color: var(--navy);
  }
  .green-band {
    position: absolute;
    left: 0;
    top: 410px;
    width: 1077px;
    height: 204px;
    background:
      radial-gradient(ellipse 360px 170px at 200px 90px, var(--green-light), rgba(127,207,159,0) 100%),
      linear-gradient(90deg, var(--green-mid), var(--green-deep));
  }
  .earth-band {
    position: absolute;
    left: 0;
    top: 614px;
    width: 1077px;
    height: 79px;
    background: var(--earth);
  }
  .web-tab {
    position: absolute;
    left: 525px;
    top: 584px;
    width: 560px;
    height: 64px;
    background: var(--navy-tab);
    border: 3px solid var(--card-white);
    border-right: none;
    border-radius: 34px 0 0 0;
  }
  .contact {
    position: absolute;
    display: flex;
    align-items: center;
    gap: 10px;
    color: var(--card-white);
    font-size: 30px;
    line-height: 32px;
  }
  .contact svg { width: 32px; height: 32px; flex: none; }
  .contact.email { left: 657px; top: 439px; }
  .contact.hashtag { left: 699px; top: 470px; }
  .contact.phone { left: 657px; top: 514px; }
  .contact.web { left: 657px; top: 604px; }
</style>
</head>
<body>
  <main class="business-card">
    <div class="cube-art-area" role="img" aria-label="Illustration of two translucent mint-green cubes"></div>

    <div class="brand-mark">
      <span class="brand-square"></span>
      <span class="brand-name">Dan Theroll</span>
    </div>

    <header class="identity">
      <h1 class="person-name">Professor Dan Theroll</h1>
      <p class="tagline">Unlocking Early Numeracy</p>
    </header>

    <div class="green-band"></div>
    <div class="earth-band"></div>
    <div class="web-tab"></div>

    <div class="contact email">
      <svg viewBox="0 0 32 32" aria-hidden="true">
        <circle cx="16" cy="16" r="15" fill="var(--card-white)"/>
        <rect x="7" y="10" width="18" height="12" fill="var(--icon-red)"/>
        <polyline points="7,10 16,17 25,10" fill="none" stroke="var(--card-white)" stroke-width="1.6"/>
      </svg>
      <span>info@dantheroll.net</span>
    </div>
    <div class="contact hashtag"><span>#dantheroll26</span></div>
    <div class="contact phone">
      <svg viewBox="0 0 32 32" aria-hidden="true">
        <circle cx="16" cy="16" r="15" fill="var(--card-white)"/>
        <path d="M11 8 l3 0 l1.5 4 l-2 1.5 q1.5 3.5 5 5 l1.5 -2 l4 1.5 l0 3 q-1 2 -3 2 q-7 -1 -11 -9 q-1 -4 1 -6 z" fill="var(--icon-red)"/>
      </svg>
      <span>+44 7812 660 394</span>
    </div>
    <div class="contact web">
      <svg viewBox="0 0 32 32" aria-hidden="true">
        <circle cx="16" cy="16" r="15" fill="var(--card-white)"/>
        <circle cx="16" cy="16" r="10" fill="none" stroke="var(--icon-red)" stroke-width="2"/>
        <ellipse cx="16" cy="16" rx="4.5" ry="10" fill="none" stroke="var(--icon-red)" stroke-width="1.6"/>
        <line x1="6" y1="16" x2="26" y2="16" stroke="var(--icon-red)" stroke-width="1.6"/>
        <line x1="8" y1="11" x2="24" y2="11" stroke="var(--icon-red)" stroke-width="1.4"/>
        <line x1="8" y1="21" x2="24" y2="21" stroke="var(--icon-red)" stroke-width="1.4"/>
      </svg>
      <span>www.dantheroll.net</span>
    </div>
  </main>
</body>
</html>
```